Billboard to promote Harwell County, NC

I would like a billboard designed for the Chamber of Commerce. The size of the board is 10'h by 24'w. I would like our logo colors used and IF space permits, include our logo. I want to board to be very easy to read with a simplistic message of #StayWithHarwell, Invest in this community, Shop, Dine, Live. I would like our web address to scroll the bottom of the board, www.TheHarwellChamber.example

Target Market(s)

Local residents and visitors

Industry/Entity Type

Chamber Of Commerce

Requirements
Must have
• Quick message
• Easy to read
• Bold type
Nice to have
• Our logo, if space permits.
Should not have
• Should not be too busy or hard to read. People are driving by at 55-65 miles per hour.

```html
<!DOCTYPE html>
<html lang="en">
<head>
<meta charset="utf-8">
<title>#StayWithHarwell Billboard</title>
<link rel="stylesheet" href="https://fonts.googleapis.com/css2?family=Crimson+Pro:wght@700;800&family=Arimo:wght@400;700&display=swap">
<style>
  :root {
    --board-center: #8e8e8e;
    --board-edge: #3b3b3b;
    --swoosh-light: #ffffff;
    --swoosh-mid: #d9d9d9;
    --swoosh-shade: #2a2a2a;
    --hashtag-top: #8fe6ff;
    --hashtag-bottom: #1fb6f0;
    --hashtag-outline: #0a5f8c;
    --message: #dedede;
    --url: #1f6f93;
    --chamber-navy: #1b3566;
    --chamber-dot: #2aa7d8;
  }
  html, body {
    margin: 0;
    padding: 0;
    overflow: hidden;
    background: #ffffff;
  }
  .billboard {
    position: relative;
    width: 1200px;
    height: 500px;
    overflow: hidden;
    background: radial-gradient(ellipse 70% 80% at 50% 38%, var(--board-center) 0%, #6a6a6a 45%, var(--board-edge) 100%);
  }
  .billboard__swoosh {
    position: absolute;
    inset: 0;
    width: 1200px;
    height: 500px;
  }
  .billboard__hashtag {
    position: absolute;
    top: 14px;
    left: 0;
    width: 100%;
    margin: 0;
    text-align: center;
    font-family: "Crimson Pro", Georgia, serif;
    font-weight: 800;
    font-size: 82px;
    line-height: 1;
    letter-spacing: 0.5px;
    color: var(--hashtag-bottom);
    background: linear-gradient(180deg, var(--hashtag-top) 0%, #49cbfa 50%, var(--hashtag-bottom) 100%);
    -webkit-background-clip: text;
    background-clip: text;
    -webkit-text-fill-color: transparent;
    -webkit-text-stroke: 1.5px var(--hashtag-outline);
    filter: drop-shadow(0 0 3px rgba(120, 220, 255, 0.9)) drop-shadow(2px 3px 2px rgba(0, 0, 0, 0.45));
  }
  .billboard__message {
    position: absolute;
    top: 170px;
    left: 58px;
    margin: 0;
    padding: 0;
    list-style: none;
    font-family: "Crimson Pro", Georgia, serif;
    font-weight: 700;
    font-size: 72px;
    line-height: 68px;
    color: var(--message);
    text-shadow: 2px 3px 3px rgba(0, 0, 0, 0.55);
  }
  .billboard__message li::before {
    content: "\2022";
    display: inline-block;
    width: 44px;
  }
  .billboard__url {
    position: absolute;
    left: 540px;
    top: 470px;
    font-family: "Arimo", Arial, sans-serif;
    font-size: 24px;
    color: var(--url);
    letter-spacing: 0.3px;
  }
  .chamber-mark {
    position: absolute;
    right: 22px;
    top: 392px;
    width: 210px;
    text-align: center;
  }
  .chamber-mark__dot {
    display: block;
    width: 44px;
    height: 44px;
    margin: 0 auto 8px;
    border-radius: 50%;
    background: var(--chamber-dot);
  }
  .chamber-mark__name {
    font-family: "Arimo", Arial, sans-serif;
    font-weight: 700;
    font-size: 14px;
    line-height: 16px;
    color: var(--chamber-navy);
    text-transform: uppercase;
  }
</style>
</head>
<body>
  <main class="billboard">
    <svg class="billboard__swoosh" viewBox="0 0 1200 500" aria-hidden="true">
      <defs>
        <linearGradient id="swooshFill" x1="0" y1="0" x2="1" y2="1">
          <stop offset="0" stop-color="var(--swoosh-mid)"/>
          <stop offset="0.5" stop-color="var(--swoosh-light)"/>
          <stop offset="1" stop-color="#eeeeee"/>
        </linearGradient>
        <linearGradient id="swooshShade" x1="0" y1="0" x2="0" y2="1">
          <stop offset="0" stop-color="var(--swoosh-shade)" stop-opacity="0.7"/>
          <stop offset="1" stop-color="var(--swoosh-shade)" stop-opacity="0"/>
        </linearGradient>
      </defs>
      <path d="M0 468 Q 640 462 1200 318 L1200 338 Q 640 478 0 482 Z" fill="url(#swooshShade)"/>
      <path d="M0 474 Q 640 470 1200 326 L1200 500 L0 500 Z" fill="url(#swooshFill)"/>
    </svg>

    <h1 class="billboard__hashtag">#StayWithHarwell</h1>

    <ul class="billboard__message">
      <li>Invest in this community</li>
      <li>Shop</li>
      <li>Dine</li>
      <li>Live</li>
    </ul>

    <div class="billboard__url">www.TheHarwellChamber.example</div>

    <div class="chamber-mark">
      <span class="chamber-mark__dot"></span>
      <div class="chamber-mark__name">Harwell Chamber<br>of Commerce &amp; Tourism</div>
    </div>
  </main>
</body>
</html>
```